Commercial Solar Flyer

We are an electrical and solar company that requires a flyer that focuses on energy efficient options available including solar that will be primarily for schools and other business owners.
I have a brief attached that gives basics including logo, pictures etc
Also attached is a recent flyer that lists additional services
This is a really urgent request.

Target Market(s)

Business decision makers - 45+ years prominently male
i.e. school principals and / or accountants

Industry/Entity Type

Electrical

Requirements
Must have
• Clutter free, not too much words
Nice to have
• Prefer 1 page A4

```html
<!DOCTYPE html>
<html lang="en">
<head>
<meta charset="utf-8">
<title>Commercial Solar Flyer – B&amp;R Halloway Electrical and Solar</title>
<link rel="stylesheet" href="https://fonts.googleapis.com/css2?family=Open+Sans:wght@400;600;700&display=swap">
<style>
  :root {
    --page-bg: #d9dadb;
    --paper: #ffffff;
    --ink: #2b2b2b;
    --ink-dark: #1f2326;
    --brand-red: #c8282b;
    --band-dark: #1e2022;
    --title-panel: rgba(40, 44, 50, 0.72);
    --sky-top: #9fc6ea;
    --sky-mid: #dfe9f1;
    --panel-blue: #2f4f8f;
    --panel-deep: #1d3469;
    --tower-tint: #e9ebed;
    --white: #ffffff;
  }
  * { box-sizing: border-box; margin: 0; padding: 0; }
  html, body { width: 870px; height: 1200px; overflow: hidden; }
  body {
    background: var(--page-bg);
    font-family: "Open Sans", Arial, sans-serif;
    color: var(--ink);
    position: relative;
  }
  .flyer {
    position: absolute;
    left: 27px; top: 25px;
    width: 816px; height: 1150px;
    background: var(--paper);
    overflow: hidden;
    box-shadow: 0 2px 8px rgba(0,0,0,0.18);
  }
  .hero-photo {
    position: absolute; left: 0; top: 0;
    width: 816px; height: 491px;
    background: linear-gradient(180deg, var(--sky-top) 0%, var(--sky-mid) 26%, #c9d3dc 32%, var(--panel-blue) 45%, var(--panel-deep) 75%, #3b5a98 100%);
  }
  .hero-divider { position: absolute; left: 0; top: 474px; width: 816px; height: 38px; }
  .brand {
    position: absolute; right: 46px; top: 52px;
    display: flex; align-items: center; gap: 12px;
  }
  .brand-mark { width: 40px; height: 40px; background: var(--brand-red); }
  .brand-name {
    font-weight: 700; font-size: 30px; letter-spacing: 0.5px;
    color: var(--ink-dark); line-height: 1;
  }
  .title-panel {
    position: absolute; left: 0; top: 207px;
    width: 566px; height: 156px;
    background: var(--title-panel);
    border-radius: 0 12px 12px 0;
    padding: 20px 0 0 36px;
    color: var(--white);
  }
  .title-panel h1 {
    font-size: 27px; font-weight: 700; line-height: 1.38; letter-spacing: 0.2px;
  }
  .title-panel p { font-size: 21px; font-weight: 400; margin-top: 4px; }
  .tower-art {
    position: absolute; left: 510px; top: 600px;
    width: 260px; height: 420px;
    background: linear-gradient(180deg, rgba(233,235,237,0) 0%, var(--tower-tint) 40%, rgba(233,235,237,0.6) 100%);
  }
  .intro {
    position: absolute; left: 53px; top: 520px; width: 520px;
  }
  .intro h2 {
    font-size: 25px; font-weight: 700; line-height: 1.4; color: var(--ink-dark);
  }
  .benefits { list-style: none; margin-top: 16px; }
  .benefits li {
    position: relative;
    padding-left: 9px;
    margin-left: 0;
    font-size: 21.5px; line-height: 34px;
    text-align: justify;
    margin-bottom: 14px;
  }
  .benefits li svg {
    position: absolute; left: -29px; top: 7px; width: 20px; height: 24px;
  }
  .footer-divider { position: absolute; left: 0; top: 1040px; width: 816px; height: 22px; }
  .footer {
    position: absolute; left: 0; top: 1052px;
    width: 816px; height: 98px;
    background: var(--brand-red);
    color: var(--white);
  }
  .footer-phone {
    position: absolute; right: 54px; top: 14px;
    display: flex; align-items: center; gap: 10px;
    font-size: 27px; font-weight: 700;
  }
  .footer-contacts {
    position: absolute; right: 44px; top: 62px;
    display: flex; gap: 40px; font-size: 18px;
  }
  .footer-contacts span { display: flex; align-items: center; gap: 8px; }
</style>
</head>
<body>
  <main class="flyer">
    <div class="hero-photo" role="img" aria-label="Photograph of a rooftop covered in rows of blue solar panels, with a white heritage building and palm trees under a blue sky"></div>

    <svg class="hero-divider" viewBox="0 0 816 38" aria-hidden="true">
      <polygon points="0,17 816,17 816,38 0,38" fill="#ffffff"/>
      <polygon points="575,0 816,0 816,17 560,17" fill="#1e2022"/>
    </svg>

    <div class="brand">
      <span class="brand-mark" aria-hidden="true"></span>
      <span class="brand-name">B&amp;R HALLOWAY</span>
    </div>

    <section class="title-panel">
      <h1>ENERGY EFFICIENT<br>ELECTRICAL AND SOLAR SERVICES</h1>
      <p>for Commercial and Residential Customers</p>
    </section>

    <div class="tower-art" role="img" aria-label="Faint line illustration of an electricity transmission tower"></div>

    <section class="intro">
      <h2>We are trying to establish that we do more that solar</h2>
      <ul class="benefits">
        <li><svg viewBox="0 0 20 24" aria-hidden="true"><polygon points="14,0 4,13 10,13 5,24 17,9 11,9" fill="#c8282b"/></svg>Our goal is to provide a customised and complete energy efficient solution to our customers rather than just a solar package like most other solar marketing companies.</li>
        <li><svg viewBox="0 0 20 24" aria-hidden="true"><polygon points="14,0 4,13 10,13 5,24 17,9 11,9" fill="#c8282b"/></svg>Electricity prices are still rising and many businesses are looking to solar as a way of controlling their ongoing costs.</li>
        <li><svg viewBox="0 0 20 24" aria-hidden="true"><polygon points="14,0 4,13 10,13 5,24 17,9 11,9" fill="#c8282b"/></svg>But there are many other ways to reduce and control costs including Power Factor Correction, Static Compensation LED Lighting and Solar Hot Water.</li>
      </ul>
    </section>

    <svg class="footer-divider" viewBox="0 0 816 22" aria-hidden="true">
      <polygon points="0,0 240,0 225,12 0,12" fill="#1e2022"/>
    </svg>

    <footer class="footer">
      <div class="footer-phone">
        <svg width="24" height="24" viewBox="0 0 24 24" aria-hidden="true"><circle cx="12" cy="12" r="10.5" fill="none" stroke="#fff" stroke-width="2"/><path d="M8.5 6.5c.6-.4 1.2-.2 1.5.4l1 2c.2.5 0 1-.4 1.3l-.7.5c.5 1.3 1.3 2.3 2.4 3l.6-.6c.4-.4 1-.5 1.4-.2l1.8 1.2c.5.4.6 1 .2 1.5-1 1.3-2.6 1.5-4 .6-2.4-1.5-4.2-3.8-4.8-6.5-.2-1.3.2-2.6 1-3.2z" fill="#fff"/></svg>
        1300 555 014
      </div>
      <div class="footer-contacts">
        <span><svg width="16" height="12" viewBox="0 0 16 12" aria-hidden="true"><rect width="16" height="12" rx="1" fill="#fff"/><polyline points="0.5,0.8 8,6.5 15.5,0.8" fill="none" stroke="#c8282b" stroke-width="1.4"/></svg>mia@halloway.com.au</span>
        <span><svg width="15" height="15" viewBox="0 0 16 16" aria-hidden="true"><g fill="none" stroke="#fff" stroke-width="1.3"><circle cx="8" cy="8" r="7"/><ellipse cx="8" cy="8" rx="3" ry="7"/><line x1="1" y1="8" x2="15" y2="8"/></g></svg>www.brhalloway.com.au</span>
      </div>
    </footer>
  </main>
</body>
</html>
```